New Stationary for our business

We are a gift business and would like to create a new corporate image with new stationary and design.

We would like a Classic Corporate look with a touch of Flair.

We would need:
Envelopes
Letter Head
Business Cards
With Comp Slips
Note Pads
Etc...

Our details are:

Basket Haven Pty Ltd
518 Tallow Street, Fernmead, Victoria, 3071
1800 742 918
www.baskethaven-demo.com.au
sales@baskethaven-demo.com.au

ABN: 58 603 214 796

Target Market(s)

Corporate Look

Industry/Entity Type

Marketing

Contact Information for Business Card

Basket Haven Pty Ltd
1800 742 918
518 Tallow Street
Fernmead 3071
Victoria Australia

Darren Pelluso - Managing Director
darren.pelluso@baskethaven-demo.com.au
0413 587 120

Logo Text

Basket Haven - The Gift Specialists

Colors

Designer to choose colors to be used in the design.

Requirements
Must have
• Look and Feel upmarket and exclusive

```html
<!DOCTYPE html>
<html lang="en">
<head>
<meta charset="utf-8">
<title>Basket Haven – Stationery Suite</title>
<link rel="stylesheet" href="https://fonts.googleapis.com/css2?family=Lato:wght@400;700;900&display=swap">
<style>
:root{
  --bg:#7b7b7b;
  --red:#c91f26;
  --red-dark:#a8181e;
  --paper:#ffffff;
  --paper-shade:#f1f1f1;
  --mark-grey:#c4c5c7;
  --ink:#333333;
  --ink-soft:#555555;
}
*{margin:0;padding:0;box-sizing:border-box}
html,body{width:1200px;height:1200px;overflow:hidden;background:var(--bg)}
body{position:relative;font-family:'Lato',sans-serif;color:var(--ink)}
.artwork{position:absolute;left:0;top:0;width:1200px;height:1200px}
.t{position:absolute;white-space:nowrap;line-height:1.2}
.brand-name{font-family:'Lato',sans-serif;font-weight:900;color:var(--red)}
.brand-name.on-red{color:#fff}
.tagline{font-family:'Lato',sans-serif;font-weight:400;text-transform:uppercase;color:var(--ink)}
.tagline.on-red,.abn.on-red{color:#fff}
.abn{font-family:'Lato',sans-serif;color:var(--ink-soft)}
.center{transform:translateX(-50%);text-align:center}
.right{transform:translateX(-100%);text-align:right}
.contact{font-size:5px;color:var(--ink);line-height:1.3}
.contact.on-red{color:#fff}
.letter-body{position:absolute;left:690px;width:160px;font-size:3.6px;line-height:1.35;color:var(--ink-soft);white-space:normal;text-align:justify}
.compliments{font-weight:900;color:#fff;font-size:7px;letter-spacing:.6px}
</style>
</head>
<body>

<svg class="artwork" viewBox="0 0 1200 1200" aria-hidden="true">
  <defs>
    <filter id="paper-shadow" x="-10%" y="-10%" width="130%" height="130%">
      <feDropShadow dx="2" dy="3" stdDeviation="3" flood-color="#000" flood-opacity=".25"/>
    </filter>
    <linearGradient id="window-glare" x1="0" y1="0" x2="1" y2="1">
      <stop offset="0" stop-color="#e2353b"/>
      <stop offset=".5" stop-color="#c91f26"/>
      <stop offset="1" stop-color="#9d151b"/>
    </linearGradient>
  </defs>

  <!-- brand header mark: plain square -->
  <rect class="header-square" x="544" y="44" width="141" height="141" fill="var(--mark-grey)"/>

  <!-- presentation folder -->
  <g class="folder" filter="url(#paper-shadow)">
    <polygon points="142,354 92,386 92,662 142,698" fill="var(--paper)"/>
    <polygon points="142,698 392,698 350,756 142,756" fill="var(--paper)"/>
    <rect x="142" y="354" width="250" height="344" fill="var(--red)"/>
    <rect x="392" y="354" width="250" height="344" fill="var(--paper)"/>
  </g>
  <rect x="491" y="481" width="46" height="46" fill="var(--mark-grey)"/>
  <line x1="620" y1="354" x2="620" y2="698" stroke="var(--red)" stroke-width="1.6"/>
  <line x1="392" y1="678" x2="642" y2="678" stroke="var(--red)" stroke-width="1.6"/>
  <rect x="549" y="665" width="5" height="5" fill="var(--red)"/>
  <!-- folder contact icons -->
  <g fill="#fff">
    <path d="M193 677 q0 5 5 5 l1-1.5 -1.5-1.2 -1 .8 q-1.6-.8-2.3-2.3 l.8-1 -1.2-1.5z"/>
    <rect x="233" y="677" width="5" height="3.6" rx=".5"/>
    <path d="M289 676 a2 2 0 1 1 0.01 0 M287.3 677 L289 681 L290.7 677z"/>
  </g>

  <!-- letterhead -->
  <rect class="letterhead" x="662" y="366" width="224" height="317" fill="var(--paper)" filter="url(#paper-shadow)"/>
  <rect x="706" y="393" width="20" height="20" fill="var(--mark-grey)"/>
  <line x1="868" y1="366" x2="868" y2="683" stroke="var(--red)" stroke-width="1.2"/>
  <line x1="662" y1="666" x2="886" y2="666" stroke="var(--red)" stroke-width="1.2"/>
  <rect role="img" aria-label="Handwritten signature" x="816" y="634" width="36" height="8" fill="#b8b8b8" opacity=".6"/>

  <!-- business card, front -->
  <rect class="card-front" x="879" y="459" width="156" height="89" fill="var(--red)" filter="url(#paper-shadow)"/>
  <rect x="944" y="478" width="26" height="26" fill="#ffffff"/>
  <!-- business card, back -->
  <rect class="card-back" x="878" y="558" width="156" height="89" fill="var(--paper)" filter="url(#paper-shadow)"/>
  <rect x="903" y="570" width="14" height="14" fill="var(--mark-grey)"/>
  <line x1="1019" y1="558" x2="1019" y2="647" stroke="var(--red)" stroke-width="1"/>
  <line x1="878" y1="635" x2="1034" y2="635" stroke="var(--red)" stroke-width="1"/>

  <!-- with compliments slip -->
  <rect class="comp-slip" x="667" y="718" width="303" height="142" fill="var(--paper)" filter="url(#paper-shadow)"/>
  <rect x="713" y="733" width="22" height="22" fill="var(--mark-grey)"/>
  <line x1="950" y1="718" x2="950" y2="860" stroke="var(--red)" stroke-width="1.4"/>
  <line x1="667" y1="839" x2="970" y2="839" stroke="var(--red)" stroke-width="1.4"/>
  <polygon points="667,832 800,832 814,848 667,848" fill="var(--red)"/>

  <!-- note pad -->
  <rect class="notepad" x="142" y="802" width="233" height="329" fill="var(--paper)" filter="url(#paper-shadow)"/>
  <rect x="186" y="822" width="26" height="26" fill="var(--mark-grey)"/>
  <line x1="361" y1="802" x2="361" y2="1131" stroke="var(--red)" stroke-width="1.4"/>
  <line x1="142" y1="1115" x2="375" y2="1115" stroke="var(--red)" stroke-width="1.4"/>

  <!-- large envelope, back -->
  <rect class="envelope-large" x="398" y="802" width="233" height="330" fill="var(--paper)" filter="url(#paper-shadow)"/>
  <path d="M398 802 H631 L627 836 Q626 840 620 840 H410 Q404 840 403 836 Z" fill="var(--red)"/>
  <rect x="505" y="810" width="24" height="24" fill="var(--mark-grey)"/>

  <!-- DL envelope, back -->
  <rect class="envelope-dl-back" x="666" y="898" width="284" height="142" fill="var(--paper)" filter="url(#paper-shadow)"/>
  <path d="M666 898 H950 L947 938 Q946 944 940 944 H676 Q670 944 669 938 Z" fill="var(--red)"/>
  <rect x="796" y="906" width="29" height="29" fill="var(--mark-grey)"/>

  <!-- DL envelope, front -->
  <rect class="envelope-dl-front" x="796" y="988" width="285" height="142" fill="var(--paper)" filter="url(#paper-shadow)"/>
  <rect x="816" y="1056" width="90" height="44" rx="9" fill="url(#window-glare)"/>
  <rect x="1011" y="1003" width="24" height="24" fill="var(--mark-grey)"/>
  <line x1="1066" y1="988" x2="1066" y2="1130" stroke="var(--red)" stroke-width="1.4"/>
  <line x1="796" y1="1114" x2="1081" y2="1114" stroke="var(--red)" stroke-width="1.4"/>
</svg>

<!-- brand header -->
<div class="t center brand-name" style="left:614px;top:196px;font-size:50px">Basket Haven</div>
<div class="t center tagline" style="left:618px;top:252px;font-size:19px;letter-spacing:13px">The Gift Specialists</div>
<div class="t center abn" style="left:614px;top:281px;font-size:17px">ABN: 58 603 214 796</div>

<!-- folder -->
<div class="t center brand-name" style="left:514px;top:530px;font-size:17px">Basket Haven</div>
<div class="t center tagline" style="left:516px;top:549px;font-size:6.5px;letter-spacing:3px">The Gift Specialists</div>
<div class="t center abn" style="left:514px;top:558px;font-size:6px">ABN: 58 603 214 796</div>
<div class="t contact" style="left:557px;top:665px">www.baskethaven-demo.com.au</div>
<div class="t contact on-red" style="left:200px;top:677px;font-size:3.6px">1800 742 918</div>
<div class="t contact on-red" style="left:241px;top:677px;font-size:3.6px">sales@baskethaven-demo.com.au</div>
<div class="t contact on-red" style="left:296px;top:676px;font-size:3.6px">518 Tallow Street, Fernmead,<br>Victoria, 3071</div>

<!-- letterhead -->
<div class="t center brand-name" style="left:716px;top:414px;font-size:7.5px">Basket Haven</div>
<div class="t center tagline" style="left:716px;top:423px;font-size:3px;letter-spacing:1.3px">The Gift Specialists</div>
<div class="t center abn" style="left:716px;top:427px;font-size:2.8px">ABN: 58 603 214 796</div>
<div class="t right contact" style="left:850px;top:397px;font-size:3.4px">8775550142<br>info@northvale-demo.com<br>Two Harbor Plaza 400 9th Street NW<br>www.northvale-demo.com</div>
<div class="t contact" style="left:690px;top:445px;font-size:3.6px"><b>Dear, Mr________</b><br><span style="font-size:2.6px">Designation<br><b>COMPANY NAME</b></span></div>
<div class="t right contact" style="left:850px;top:445px;font-size:3.6px"><b>DATE:1/3/2018</b></div>
<p class="letter-body" style="top:472px">Thank you for choosing us for your gifting needs. Every hamper is packed by hand with care and quality produce.</p>
<p class="letter-body" style="top:509px">Thank you for choosing us for your gifting needs. Every hamper is packed by hand with care and quality produce.</p>
<p class="letter-body" style="top:546px">Thank you for choosing us for your gifting needs. Every hamper is packed by hand with care and quality produce.</p>
<p class="letter-body" style="top:583px">Thank you for choosing us for your gifting needs. Every hamper is packed by hand with care and quality produce.</p>
<div class="t right contact" style="left:850px;top:621px;font-size:4px"><b>YOUR NAME</b><br><span style="font-size:2.8px">Designation</span></div>

<!-- business card front -->
<div class="t center brand-name on-red" style="left:957px;top:506px;font-size:10px">Basket Haven</div>
<div class="t center tagline on-red" style="left:958px;top:518px;font-size:3.6px;letter-spacing:1.6px">The Gift Specialists</div>
<div class="t center abn on-red" style="left:957px;top:523px;font-size:3px">ABN: 58 603 214 796</div>

<!-- business card back -->
<div class="t center brand-name" style="left:910px;top:585px;font-size:5.6px">Basket Haven</div>
<div class="t center tagline" style="left:910px;top:592px;font-size:2.4px;letter-spacing:.9px">The Gift Specialists</div>
<div class="t contact" style="left:893px;top:606px;font-size:2.8px;line-height:1.45">Darren Pelluso – Managing Director<br>1800 742 918 · 0413 587 120<br>darren.pelluso@baskethaven-demo.com.au<br>518 Tallow Street, Fernmead 3071, Victoria Australia</div>

<!-- compliments slip -->
<div class="t center brand-name" style="left:724px;top:756px;font-size:8px">Basket Haven</div>
<div class="t center tagline" style="left:724px;top:765px;font-size:3px;letter-spacing:1.4px">The Gift Specialists</div>
<div class="t center abn" style="left:724px;top:769px;font-size:2.8px">ABN: 58 603 214 796</div>
<div class="t contact" style="left:692px;top:791px;font-size:5px">1800 742 918<br>sales@baskethaven-demo.com.au<br>518 Tallow Street, Fernmead,<br>Victoria, 3071<br>www.baskethaven-demo.com.au</div>
<div class="t compliments" style="left:692px;top:835px">WITH COMPLIMENTS</div>

<!-- note pad -->
<div class="t center brand-name" style="left:199px;top:849px;font-size:9px">Basket Haven</div>
<div class="t center tagline" style="left:199px;top:859px;font-size:3.4px;letter-spacing:1.6px">The Gift Specialists</div>
<div class="t center abn" style="left:199px;top:864px;font-size:3px">ABN: 58 603 214 796</div>

<!-- large envelope -->
<div class="t contact" style="left:418px;top:1085px;font-size:4.6px">1800 742 918<br>sales@baskethaven-demo.com.au<br>518 Tallow Street, Fernmead,<br>Victoria, 3071<br>www.baskethaven-demo.com.au</div>

<!-- DL envelope front -->
<div class="t center brand-name" style="left:1023px;top:1027px;font-size:8px">Basket Haven</div>
<div class="t center tagline" style="left:1023px;top:1036px;font-size:3px;letter-spacing:1.4px">The Gift Specialists</div>
<div class="t center abn" style="left:1023px;top:1040px;font-size:2.8px">ABN: 58 603 214 796</div>
<div class="t right contact" style="left:1054px;top:1067px;font-size:5px">1800 742 918<br>sales@baskethaven-demo.com.au<br>518 Tallow Street, Fernmead,<br>Victoria, 3071<br>www.baskethaven-demo.com.au</div>

</body>
</html>
```